Educational Textbook Covern Design for mostly females

Create a textbook cover (will be white spiral) using the Brandguide.pdf attached. This will be a textbook given to mostly age 18-25 year old women so a modern trendy cute type design is wanted.
The book cover is 8.5" x 11" which will be printed in CMYK full bleed.
The name "LoriPQX's Dental Hygiene Academy" must be on the cover somewhere and "LoriPQX" has to be either the same height or larger height than the "Dental Hygiene Academy"

Please no real life photos such as images of dentists, etc. This should be all created art.

The year "2025" should be in the design as well.

IMPORTANT UPDATED 8/4/2024
These designs should not look too childish. This should be a professional textbook for dental professionals. All the current designs have too much cartoon art.

Target Market(s)

18-25 year old females

Industry/Entity Type

Dentistry

Font styles to use
Other font styles liked:
• See brand guide

Colors
A7469A
B969AE
D3A5CF
EDDBEB
F8F0F9
6B429C
8869AF
B7A5CE
E3DAEB
F3F0F8

Requirements
Should not have
• No photos, should be all art

```html
<!DOCTYPE html>
<html lang="en">
<head>
<meta charset="utf-8">
<title>LoriPQX's Dental Hygiene Academy – 2025 Textbook Covers</title>
<link rel="stylesheet" href="https://fonts.googleapis.com/css2?family=Fredoka:wght@500;600;700&family=Roboto:wght@400;500;700&display=swap">
<style>
  :root {
    --stage: #b1b1b0;
    --purple: #472a7a;
    --purple-deep: #43266f;
    --yellow: #e7cf34;
    --lilac: #9b7bbc;
    --white: #ffffff;
    --icon-blue: #6fc2ea;
    --ink-light: #f2eef8;
  }
  * { box-sizing: border-box; margin: 0; padding: 0; }
  html, body { width: 969px; height: 1200px; overflow: hidden; }
  body {
    background: var(--stage);
    position: relative;
    font-family: "Roboto", Arial, sans-serif;
  }
  .cover {
    position: absolute;
    top: 322px;
    width: 430px;
    height: 556px;
  }
  .cover--back { left: 39px; background: var(--purple); }
  .cover--front { left: 500px; background: var(--white); }

  /* Back cover */
  .brand-mark {
    position: absolute;
    left: 0; right: 0; top: 98px;
    display: flex; flex-direction: column; align-items: center; gap: 10px;
  }
  .brand-mark__dot {
    width: 46px; height: 46px; border-radius: 50%;
    background: var(--yellow);
  }
  .brand-mark__name {
    font-family: "Fredoka", Arial, sans-serif;
    font-weight: 600; font-size: 30px;
    color: var(--yellow);
  }
  .contact {
    position: absolute;
    left: 0; width: 420px; top: 234px;
    display: flex; flex-direction: column; align-items: center;
    color: var(--ink-light);
    text-align: center;
  }
  .contact__title {
    font-family: "Fredoka", Arial, sans-serif;
    font-weight: 600; font-size: 8.5px; letter-spacing: 0.2px;
    margin-bottom: 12px;
  }
  .contact__icon { width: 16px; height: 18px; margin-bottom: 7px; }
  .contact__label { font-weight: 700; font-size: 6px; margin-bottom: 7px; }
  .contact__value { font-size: 5.5px; line-height: 8px; margin-bottom: 14px; }

  /* Front cover */
  .badge {
    position: absolute;
    border-radius: 50%;
  }
  .badge--purple { background: var(--purple-deep); }
  .badge--yellow { background: var(--yellow); }
  .badge--lilac { background: var(--lilac); }
  .badge--side { width: 75px; height: 75px; left: 44px; }
  .badge--hero { width: 113px; height: 113px; left: 213px; top: 138px; }

  .title {
    position: absolute;
    left: 140px; width: 290px; top: 256px;
    text-align: center;
    color: var(--purple);
    font-family: "Fredoka", Arial, sans-serif;
    font-weight: 600;
  }
  .title__name { display: block; font-size: 44px; line-height: 1; letter-spacing: 0.5px; }
  .title__school { display: block; font-size: 14.5px; line-height: 1.2; margin-top: 2px; letter-spacing: 0.3px; }
  .year {
    position: absolute;
    left: 140px; width: 290px; top: 364px;
    text-align: center;
    font-family: "Fredoka", Arial, sans-serif;
    font-weight: 700; font-size: 40px;
    color: var(--purple);
  }
</style>
</head>
<body>

<section class="cover cover--back" aria-label="Back cover">
  <div class="brand-mark">
    <div class="brand-mark__dot"></div>
    <div class="brand-mark__name">LoriPQX's</div>
  </div>

  <div class="contact">
    <div class="contact__title">Contact Info:</div>

    <svg class="contact__icon" viewBox="0 0 16 18" fill="none" stroke="var(--icon-blue)" stroke-width="0.9">
      <path d="M8 17 C4 12 2.5 9 2.5 6.5 A5.5 5.5 0 0 1 13.5 6.5 C13.5 9 12 12 8 17 Z"/>
      <circle cx="8" cy="6.5" r="1.8"/>
    </svg>
    <div class="contact__label">Address:</div>
    <div class="contact__value">Riverton, Georgia</div>

    <svg class="contact__icon" viewBox="0 0 20 18" fill="none" stroke="var(--icon-blue)" stroke-width="0.9">
      <rect x="6.5" y="1" width="7" height="16" rx="1"/>
      <line x1="6.5" y1="3.5" x2="13.5" y2="3.5"/>
      <line x1="6.5" y1="14" x2="13.5" y2="14"/>
      <circle cx="10" cy="15.6" r="0.6"/>
      <path d="M4.5 5 Q3 7 4.5 9 M2.5 4 Q0.5 7 2.5 10"/>
      <path d="M15.5 5 Q17 7 15.5 9 M17.5 4 Q19.5 7 17.5 10"/>
    </svg>
    <div class="contact__label">Phone:</div>
    <div class="contact__value">555-014-LORI<br>TEXT OR PHONE</div>

    <svg class="contact__icon" viewBox="0 0 18 14" fill="none" stroke="var(--icon-blue)" stroke-width="0.9">
      <rect x="1" y="1.5" width="16" height="11"/>
      <path d="M1 1.5 L9 8 L17 1.5 M1 12.5 L7 6.5 M17 12.5 L11 6.5"/>
    </svg>
    <div class="contact__label">Email:</div>
    <div class="contact__value">lori@loripqxreview.com</div>
  </div>
</section>

<section class="cover cover--front" aria-label="Front cover">
  <div class="badge badge--side badge--purple" style="top:63px" role="img" aria-label="Illustration: tooth character with a speech bubble and microphone"></div>
  <div class="badge badge--side badge--yellow" style="top:150px" role="img" aria-label="Illustration: tooth character celebrating with a party hat"></div>
  <div class="badge badge--side badge--purple" style="top:238px" role="img" aria-label="Illustration: tooth character with a light bulb idea"></div>
  <div class="badge badge--side badge--yellow" style="top:325px" role="img" aria-label="Illustration: tooth character in a graduation cap with diploma"></div>
  <div class="badge badge--side badge--lilac" style="top:411px" role="img" aria-label="Illustration: tooth character reading a book"></div>

  <div class="badge badge--hero badge--purple" role="img" aria-label="Illustration: tooth character holding a toothbrush and pencil"></div>

  <h1 class="title">
    <span class="title__name">LoriPQX's</span>
    <span class="title__school">Dental Hygiene Academy</span>
  </h1>
  <div class="year">2025</div>
</section>

</body>
</html>
```